Business Card Design

Recruitment Company. Want to keep the logo and the green colour

Industry/Entity Type

Business

Contact Information for Business Card

Hi,

1.)
MARTIN HOLLOWAY
Director
Level 6, 248 Finch Street
Brisbane QLD 4000
M 0412 630 574
E martin@tallonstaffing.com.au
www.tallonstaffing.com.au

2.)
TOM WAVERLEY
Director
Level 6, 248 Finch Street
Brisbane QLD 4000
M 0419 247 613
E tom@tallonstaffing.com.au

Want something different and eye catching, happy for you guys to use your design flare to work some magic with these.

Many Thanks
Tom

```html
<!DOCTYPE html>
<html lang="en">
<head>
<meta charset="utf-8">
<title>Tallon Staffing — Business Card</title>
<link rel="stylesheet" href="https://fonts.googleapis.com/css2?family=Arimo:wght@400;700&display=swap">
<style>
  :root {
    --backdrop: #e4e4e2;
    --card: #ffffff;
    --brand-green: #5dbb3a;
    --name-green: #8cc63f;
    --ink: #2b2b2b;
    --ink-soft: #555555;
  }
  * { margin: 0; padding: 0; box-sizing: border-box; }
  html, body {
    width: 1200px;
    height: 856px;
    overflow: hidden;
    background: var(--backdrop);
  }
  .stage {
    width: 1200px;
    height: 856px;
    display: flex;
    align-items: center;
    justify-content: center;
  }
  .business-card {
    position: relative;
    width: 840px;
    height: 480px;
    background: var(--card);
    border-radius: 38px;
    box-shadow: 0 2px 10px rgba(0,0,0,0.08);
    font-family: "Arimo", Arial, sans-serif;
    color: var(--ink);
    overflow: hidden;
  }
  .brand {
    position: absolute;
    left: 96px;
    top: 138px;
    width: 300px;
    display: flex;
    align-items: flex-start;
    gap: 14px;
  }
  .brand-dot {
    flex: none;
    width: 24px;
    height: 24px;
    margin-top: 12px;
    border-radius: 50%;
    background: var(--brand-green);
  }
  .brand-name {
    font-size: 46px;
    font-weight: 700;
    color: var(--brand-green);
    line-height: 1.02;
  }
  .brand-name span { display: block; }
  .contact {
    position: absolute;
    left: 430px;
    top: 150px;
    width: 370px;
    font-size: 19px;
    line-height: 1.3;
  }
  .contact-name {
    font-weight: 700;
    color: var(--name-green);
    font-size: 20px;
    letter-spacing: 0.3px;
  }
  .contact-role {
    color: var(--ink-soft);
    margin-bottom: 24px;
  }
  .contact-details p { margin: 0; white-space: nowrap; }
</style>
</head>
<body>
  <main class="stage">
    <article class="business-card">
      <div class="brand">
        <span class="brand-dot" aria-hidden="true"></span>
        <p class="brand-name"><span>Tallon</span><span>Staffing</span></p>
      </div>
      <section class="contact">
        <p class="contact-name">MARTIN HOLLOWAY</p>
        <p class="contact-role">Director</p>
        <div class="contact-details">
          <p>Level 6, 248 Finch Street Brisbane</p>
          <p>QLD 4000</p>
          <p>M 0412 630 574 E</p>
          <p>martin@tallonstaffing.com.au</p>
          <p>www.tallonstaffing.com.au</p>
        </div>
      </section>
    </article>
  </main>
</body>
</html>
```